iOS app design for movie reviews app

I need an app redesign for 5 pages of my iphone app. The app is a social movie reviews app that lets you share and find movies based on friends recommendations. The app is currently live in the app store under the working name tomsDeck, but I will be re-branding under the name "zested". Reviews will now be called "quips". The app is free in the app store and is a good reference for the functionality. Some screenshots can be seen here: https://apps.example-store.com/us/app/tomsdeck/id927461503?mt=8
The 5 pages should have a similar look and feel and do not have to match what is currently live in the app store. I am looking to do an overhaul of the design and am open to completely new designs, this includes color scheme.
1. Splash Screen - page users see when they initially open the app to login. Should include the name of the app (zested) and login with friendhub button, as well as graphics or a logo. Current design should be ignored.
2. Home Page (screenshot #2 on appvault page) - page user sees when they login after their first session. This is where users will normally land and is the primary place users navigate the app. The homepage must have a few elements: searchbar to find movies, user stats (quips, followers, # of time other users have read your quips, # of times other users have viewed your profile page), and six icons to navigate (watchlist, explore, popular, messages, network and my reviews). Watchlist, messages and network icons will have notification messages that come up to show when the user has new activity on those pages. There are currently icons for some of these in the app, but I am open to redesigns of these as well
3. Movie Profile Page - this is a new page to the app where a user can see more detailed information about a specific movie. This page must include poster image, title, genre, release date, rating (PG, R, etc.), length, description, video trailer and actors. A user will get to this page by tapping on the short description on the movie page (screenshot #1 on appvault page) above their friends reviews. This page will not have any reviews, just details about the movie.
4. Explore Page - this is the page where users can perform a specific search for movies. There are two filters that need to be accessible (location of movie and genre). A user can perform a search just for themself and filter by movies they have seen or never seen. They can also search for movies that they want to watch with a friend, so they select a friend and see results that both of them would like.
5. My Reviews Page (screenshot #4 on appvault page)- this page shows all the reviews (quips) that a user has submitted. This is just their number rating as well as the number of views that review has collected from other users. They can be sorted by top rated or most viewed.
Optional: I will also need an app icon that matches the look and feel of the app.
Movie

```html
<!DOCTYPE html>
<html lang="en">
<head>
<meta charset="utf-8">
<title>Zested — Splash Screen</title>
<link href="https://fonts.googleapis.com/css2?family=Nunito:wght@800&family=Arimo:wght@700&display=swap" rel="stylesheet">
<style>
  :root {
    --canvas-bg: #ffffff;
    --screen-blue-light: #2b93f5;
    --screen-blue-mid: #1479e6;
    --screen-blue-deep: #0a5ec7;
    --text-white: #ffffff;
    --art-dark: #2a2d33;
    --art-mid: #4a4f58;
    --art-light: #9aa3ad;
    --button-top: #ffffff;
    --button-bottom: #e4e8ee;
    --button-text: #3d5a98;
  }
  * { box-sizing: border-box; margin: 0; padding: 0; }
  html, body {
    width: 900px;
    height: 1200px;
    overflow: hidden;
    background: var(--canvas-bg);
  }
  .splash-screen {
    position: absolute;
    left: 112px;
    top: 0;
    width: 676px;
    height: 1200px;
    overflow: hidden;
    background: radial-gradient(ellipse 75% 60% at 50% 48%,
      var(--screen-blue-light) 0%,
      var(--screen-blue-mid) 55%,
      var(--screen-blue-deep) 100%);
  }
  .hero-art {
    position: absolute;
    left: 203px;
    top: 263px;
    width: 260px;
    height: 289px;
    border-radius: 12px;
    background: linear-gradient(160deg, var(--art-mid) 0%, var(--art-dark) 60%, var(--art-light) 100%);
    opacity: 0.9;
  }
  .app-name {
    position: absolute;
    left: 0;
    right: 0;
    top: 548px;
    text-align: center;
    font-family: "Nunito", sans-serif;
    font-weight: 800;
    font-size: 128px;
    line-height: 1;
    letter-spacing: -3px;
    color: var(--text-white);
  }
  .tagline {
    position: absolute;
    left: 0;
    right: 0;
    top: 700px;
    text-align: center;
    font-family: "Arimo", sans-serif;
    font-weight: 700;
    font-size: 23px;
    color: var(--text-white);
  }
  .login-button {
    position: absolute;
    left: 99px;
    top: 988px;
    width: 479px;
    height: 87px;
    border-radius: 6px;
    background: linear-gradient(180deg, var(--button-top) 0%, var(--button-top) 45%, var(--button-bottom) 100%);
    box-shadow: 0 2px 4px rgba(0, 30, 80, 0.35);
    display: flex;
    align-items: center;
    justify-content: center;
    font-family: "Arimo", sans-serif;
    font-weight: 700;
    font-size: 31px;
    letter-spacing: -0.5px;
    color: var(--button-text);
  }
</style>
</head>
<body>
  <main class="splash-screen">
    <div class="hero-art" role="img" aria-label="Illustration of a film clapperboard with a magnifying glass"></div>
    <h1 class="app-name">Zested</h1>
    <p class="tagline">The movie review app</p>
    <div class="login-button">Connect with Friendhub</div>
  </main>
</body>
</html>
```